Meridale Sonography Academy (Meridale Institute of Scan Studies) needs an additional web design f

Don't require a redesign of our existing website, I need an additional web design to compliment and feed into our existing web page (kplv.edu.au) but establish excellent google rankings in it's own right. Web page is to appeal to a specific target market in the allied health industry who wish to learn how to do ultrasound on patients. New website is www. rapidsonarskillsnet.com.au. Our educational institution delivers hands on workshops and seminars on ANYTHING involved with EMERGENCY Ultrasound - intro, advanced, doctors, nurses, etc. Our competitors in this field www.scanlearnhub.com.au and www.bqo.edu.au. Looking for a design that will capture the target audience and deliver the message that the courses are delivered by one of the best faculties in Australia. SEO strategies are paramount in that we don't wish to be penalised by Google by running a feeder site. Courses are delivered in Sydney and are accredited by an organisation called TVRE.com.au. The courses are listed under 2 qualifications on TVRE website - PLDX and RWMTZ. Registrants of our courses are striving to achieve either PLDX - Diploma in Bedside Operator Scan Skills http://www.tvre.com.au/newsite/Files/Documents/Education/PLDX/PLDX_Course_Brochure.pdf OR RWMTZ - Diploma in Support Staff Operated Scan Skills http://www.tvre.com.au/newsite/Files/Documents/Education/RWMTZ/RWMTZ_Course_Brochure.pdf.
Website to be iphone, smartphone and tablet compatible.

Target Market(s)

Emergency Physicians and Emergency nurses/doctors.

Industry/Entity Type

School

Coding

Coded - Design and coding required

Number of Pages Required

2 page

Font styles to use
Other font styles liked:
• See website http://www.brightfolddental.com.au/

Colors
86cae6
ec1f27

Requirements
Must have
• Overall professional feel but easy to read and informative.
• Links to our normal website pages www.kplv.edu.au
• Ability to rank high.
• Copy of material we deliver here http://www.kplv.edu.au/acute-scan-class-1-3-days/ Click through on relevant dates for more information.
Nice to have
• I like this website - font, feel, layout etc.
• http://www.brightfolddental.com.au/
Should not have
• Information that will lower our google rankings knowing it is linked to www.kplv.edu.au

```html
<!DOCTYPE html>
<html lang="en">
<head>
<meta charset="utf-8">
<title>Rapid Sonar Skills Network – Emergency Ultrasound Seminars</title>
<link rel="stylesheet" href="https://fonts.googleapis.com/css2?family=Nunito+Sans:wght@400;600;700;800;900&family=Open+Sans:wght@400;600&display=swap">
<style>
:root{
  --blue:#0a4f9e;
  --blue-dark:#073a78;
  --blue-footer:#0b4c99;
  --blue-bottom:#0a3a72;
  --red:#e14a2a;
  --olive:#9aa85a;
  --green:#5aa52c;
  --ink:#222;
  --grey:#555;
  --white:#fff;
}
*{box-sizing:border-box;margin:0;padding:0}
html,body{width:1200px;height:2338px;overflow:hidden}
body{font-family:"Open Sans",sans-serif;color:var(--ink);background:var(--white);position:relative}
a{color:inherit;text-decoration:none}
ul{list-style:none}

.topbar{height:39px;background:var(--blue);color:var(--white);font-size:11.5px;display:flex;align-items:center;justify-content:space-between;padding:0 47px;letter-spacing:.3px}
.topbar .sep{margin:0 14px}

.site-header{height:128px;display:flex;align-items:center;justify-content:space-between;padding:0 47px}
.brand{font-family:"Nunito Sans",sans-serif;font-weight:800;color:var(--blue);font-size:19px;line-height:24px;width:260px;margin-top:-16px}
.main-nav{display:flex;gap:0;align-self:stretch}
.main-nav a{font-family:"Nunito Sans",sans-serif;font-weight:600;font-size:14px;color:var(--ink);display:flex;align-items:center;padding:0 21px;position:relative;height:100%}
.main-nav a:last-child{padding-right:0}
.main-nav a.active{color:var(--blue)}
.main-nav a.active::after{content:"";position:absolute;left:21px;right:21px;bottom:16px;height:5px;background:var(--blue)}

.hero{height:391px;position:relative;background:linear-gradient(100deg,#d9d6d0 0%,#cfc7bd 35%,#d8cdbf 60%,#efe8e0 80%,#f3efe9 100%);overflow:hidden}
.hero-copy{position:absolute;left:0;right:0;top:105px;text-align:center}
.hero-copy h1{font-family:"Nunito Sans",sans-serif;font-weight:900;font-size:54px;color:var(--blue);line-height:1}
.hero-copy p{font-size:20px;color:#2a2a2a;margin-top:14px}
.btn{display:inline-block;background:var(--blue);color:var(--white);font-size:15px;padding:16px 22px;border-radius:4px;margin-top:22px;box-shadow:0 2px 0 var(--blue-dark)}
.dots{position:absolute;left:0;right:0;top:325px;display:flex;justify-content:center;gap:10px}
.dots span{width:12px;height:12px;border-radius:50%;border:2px solid var(--white)}
.dots span.on{background:var(--white);box-shadow:inset 0 0 0 2px #999}

.seminars{text-align:center;padding-top:44px;height:177px}
.section-title{font-family:"Nunito Sans",sans-serif;font-weight:800;color:var(--blue);font-size:21px}
.seminars p{font-size:14.5px;margin-top:12px;text-transform:uppercase}

.cards{display:flex;justify-content:space-between;padding:0 52px 0 45px}
.card{width:533px}
.card h3{height:101px;display:flex;align-items:center;padding-left:27px;color:var(--white);font-family:"Nunito Sans",sans-serif;font-weight:700;font-size:27px}
.card--pldx h3{background:var(--red)}
.card--rwmtz h3{background:var(--olive)}
.card .photo{height:281px}
.card--pldx .photo{background:linear-gradient(135deg,#e9eef2,#c9d3da 55%,#f2f2f2)}
.card--rwmtz .photo{background:linear-gradient(90deg,#5b6a1e,#d9ddd7 30%,#efefee 50%,#cf7a4a 62%,#6a7a30)}

.features{display:flex;padding:50px 45px 0 47px;height:228px}
.features-intro{width:460px}
.features-intro h2{font-family:"Nunito Sans",sans-serif;font-weight:800;color:var(--blue);font-size:21px;margin-bottom:20px}
.features-intro p{font-size:11.5px;line-height:19px;color:var(--grey)}
.feature-list{margin-left:90px;display:grid;grid-template-columns:330px 280px;row-gap:25px;margin-top:24px;column-gap:0}
.feature-list li{display:flex;align-items:center;gap:12px;color:var(--blue);font-family:"Nunito Sans",sans-serif;font-weight:700;font-size:15px}
.feature-list svg{flex:none}

.course-band{height:290px;background:linear-gradient(100deg,#2f6f9e 0%,#4e86ad 40%,#6c95b1 75%,#8aa6b8 100%);color:var(--white);text-align:center;padding-top:72px}
.course-band h2{font-family:"Nunito Sans",sans-serif;font-weight:700;font-size:30px;letter-spacing:.5px}
.course-band ul{margin-top:24px;font-size:19.5px;line-height:25px}

.booking{display:flex;padding:65px 45px 0 44px;height:367px}
.booking .photo{width:408px;height:262px;border:1px solid #ddd;padding:6px;background:var(--white)}
.booking .photo div{width:100%;height:100%;background:linear-gradient(120deg,#d9dde2,#8a8f97 45%,#3b3f48 70%,#c7b8a4)}
.booking-copy{margin-left:70px;padding-top:0}
.booking-copy h2{font-family:"Nunito Sans",sans-serif;font-weight:600;font-size:32px;color:#1a1a1a;letter-spacing:.5px}
.booking-copy p{font-size:13.5px;line-height:25px;margin-top:22px;width:600px;color:#222}
.dates{margin-top:22px;font-size:16px;line-height:26px;color:#222;margin-left:-4px}

.site-footer{height:252px;background:var(--blue-footer);display:flex;padding:38px 0 0 47px;color:var(--white)}
.footer-col{position:relative}
.footer-col + .footer-col::before{content:"";position:absolute;left:-32px;top:-20px;height:200px;width:1px;background:rgba(255,255,255,.12)}
.footer-col h4{font-family:"Nunito Sans",sans-serif;font-weight:700;font-size:21px;letter-spacing:.5px;margin-bottom:14px}
.footer-col li{font-size:12px;line-height:20.5px}
.col-about{width:288px}
.col-sono{width:307px}
.col-info{width:274px}

.bottombar{height:84px;background:var(--blue-bottom);display:flex;align-items:center;justify-content:space-between;padding:0 47px;color:var(--white);font-size:12px}
.social{display:flex;gap:22px}
.social span{width:12px;height:12px;border-radius:50%;background:var(--white);opacity:.9}
</style>
</head>
<body>

<div class="topbar">
  <span>LEVEL 3, 48 TARROW LANE, KELLSFORD</span>
  <span>EMAIL: INFO@RAPIDSONARSKILLSNET.COM.AU<span class="sep">|</span>+ 61 2 5550 1384</span>
</div>

<header class="site-header">
  <a class="brand" href="#">RAPID SONAR SKILLS NETWORK</a>
  <nav class="main-nav">
    <a class="active" href="#">ABOUT US</a>
    <a href="#">SEMINARS</a>
    <a href="#">BECOME A SONOGRAPHER</a>
    <a href="#">CONSULTING</a>
    <a href="#">MODELS</a>
    <a href="#">CONTACT US</a>
  </nav>
</header>

<section class="hero" role="img" aria-label="Clinician performing an ultrasound scan on a young patient beside an ultrasound machine">
  <div class="hero-copy">
    <h1>PLDX &amp; RWMTZ</h1>
    <p>We delivers hands on workshops and seminars on anything invoed</p>
    <a class="btn" href="#">Find Out More</a>
  </div>
  <div class="dots"><span class="on"></span><span></span><span></span></div>
</section>

<section class="seminars">
  <h2 class="section-title">OUR SEMINARS</h2>
  <p>Meridale Institute of Scan Studies and Scan Commons</p>
</section>

<section class="cards">
  <article class="card card--pldx">
    <h3>PLDX</h3>
    <div class="photo" role="img" aria-label="Doctor scanning a patient with an ultrasound probe"></div>
  </article>
  <article class="card card--rwmtz">
    <h3>RWMTZ</h3>
    <div class="photo" role="img" aria-label="Interior of an ambulance with a stretcher"></div>
  </article>
</section>

<section class="features">
  <div class="features-intro">
    <h2>OUR FEATURES:</h2>
    <p>Sed ut perspiciatis unde omnis iste natus error sit voluptatem accusantium dolo&shy;remque laudantium, totam rem aperiam, eaque ipsa quae ab illo inventore veri&shy;tatis et quasi architecto beatae vitae dicta sunt explicabo.</p>
  </div>
  <ul class="feature-list">
    <li><svg width="18" height="15" viewBox="0 0 18 15"><path d="M1 8l5 5L17 1" fill="none" stroke="var(--green)" stroke-width="3"/></svg>Online Lectures – Prerequisite physics</li>
    <li><svg width="18" height="15" viewBox="0 0 18 15"><path d="M1 8l5 5L17 1" fill="none" stroke="var(--green)" stroke-width="3"/></svg>Maximal hands on scanning time</li>
    <li><svg width="18" height="15" viewBox="0 0 18 15"><path d="M1 8l5 5L17 1" fill="none" stroke="var(--green)" stroke-width="3"/></svg>Structured Reports</li>
    <li style="margin-left:-38px"><svg width="18" height="15" viewBox="0 0 18 15"><path d="M1 8l5 5L17 1" fill="none" stroke="var(--green)" stroke-width="3"/></svg>Opportunity for Logbook submission</li>
  </ul>
</section>

<section class="course-band" role="img" aria-label="Blue background with a globe and a stethoscope">
  <h2>EMERGENCY ULTRASOUND COURSE</h2>
  <ul>
    <li>Emergency Physicians (with post graduate Ultrasound qualifications)</li>
    <li>Sonographers</li>
    <li>Medical Educationalists</li>
  </ul>
</section>

<section class="booking">
  <div class="photo"><div role="img" aria-label="Group of medical professionals around a meeting table"></div></div>
  <div class="booking-copy">
    <h2>BOOK THIS SEMINAR:</h2>
    <p>This course has been accredited by CEMQ and TVRE for AAA, E-FAST, Vascular Access, DVT and Basic Cardiac. Please see Scan Commons for accreditation details.</p>
    <ul class="dates">
      <li>29/01/2015 from 8:00 AM to 30/01/2015 3:00 PM</li>
      <li>14/05/2015 from 8:00 AM to 15/05/2015 3:00 PM</li>
      <li>03/09/2015 from 8:00 AM to 04/09/2015 3:00 PM</li>
    </ul>
  </div>
</section>

<footer class="site-footer">
  <div class="footer-col col-about">
    <h4>ABOUT</h4>
    <ul><li>About Us</li><li>Guarantee</li><li>Facilities</li><li>History</li><li>Privacy Policy</li></ul>
  </div>
  <div class="footer-col col-sono">
    <h4>SONOGRAPHY</h4>
    <ul><li>GFRT Program Overview</li><li>IQMP Program Overview</li><li>IQMP Trainee Testimonials</li><li>Meet some past students</li></ul>
  </div>
  <div class="footer-col col-info">
    <h4>INFORMATION</h4>
    <ul><li>Accommodation</li><li>Local Information</li><li>Useful Links</li><li>Venue Information</li></ul>
  </div>
  <div class="footer-col col-contact">
    <h4>CONTACT US</h4>
    <ul>
      <li>Level 3, 48 Tarrow Lane, Kellsford</li>
      <li>Kellsford NSW, 2191</li>
      <li>&nbsp;</li>
      <li>Phone: + 61 2 5550 1384</li>
      <li>Fax: + 61 2 5550 1390</li>
      <li>Email: admin@kplv.edu.au</li>
    </ul>
  </div>
</footer>

<div class="bottombar">
  <span>Copyright 2014, rapid sonar skills network. All rights reserved.</span>
  <div class="social" aria-label="Social links"><span></span><span></span><span></span><span></span><span></span><span></span><span></span></div>
</div>

</body>
</html>
```